FERNGATE BUILDERS Van Wrap Design

Ferngate builders is looking for a new vehicle wrap for our trade vans
Needs to have our LOGO, PHONE NUMBER (02278619405) QTC LOGO, CRAFT TRADES GUILD LOGO
Something big bold and attractive. The windows are tinted black but could be wrapped in white to continue the design
I have attached some ideas - we would like half wrap or full wrap

(I have attached our OLD van wrap with our OLD logo only for reference - do not copy as this is outdated)

```html
<!DOCTYPE html>
<html lang="en">
<head>
<meta charset="utf-8">
<title>Ferngate Builders – Van Wrap</title>
<link href="https://fonts.googleapis.com/css2?family=Montserrat:wght@600&family=Roboto:wght@700&display=swap" rel="stylesheet">
<style>
  :root {
    --bg: #ffffff;
    --wrap-red: #cf1f2a;
    --wrap-grey: #e4e4e4;
    --wrap-black: #0d0d0d;
    --glass: #2a0a0c;
    --trim: #1a1a1a;
    --rim: #c9c9c9;
    --ink: #1f1f1f;
    --badge: #3a3a3a;
    --white: #ffffff;
  }
  html, body {
    margin: 0;
    padding: 0;
    width: 1200px;
    height: 1200px;
    overflow: hidden;
    background: var(--bg);
  }
  .wrap-canvas {
    width: 1200px;
    height: 1200px;
    display: block;
  }
  .brand-name {
    font-family: "Montserrat", sans-serif;
    font-weight: 600;
    fill: var(--ink);
    letter-spacing: 4px;
  }
  .phone-number {
    font-family: "Roboto", sans-serif;
    font-weight: 700;
    fill: var(--white);
    font-size: 19px;
  }
</style>
</head>
<body>
<svg class="wrap-canvas" viewBox="0 0 960 960" xmlns="http://www.w3.org/2000/svg" role="img" aria-label="Ferngate Builders van side wrap">
  <defs>
    <clipPath id="van-body">
      <path d="M52 600 L55 440 L62 350 Q66 328 90 326 L630 328 Q660 330 690 350 L780 405 Q860 440 900 470 Q914 485 914 520 L914 590 Q912 604 898 606 L60 606 Q52 606 52 600 Z"/>
    </clipPath>
  </defs>

  <g class="van-panel" clip-path="url(#van-body)">
    <rect class="panel-base" x="40" y="310" width="890" height="310" fill="var(--wrap-grey)"/>
    <path class="panel-red-top" d="M40 310 L660 310 L660 330 C610 360 560 410 505 446 L40 446 Z" fill="var(--wrap-red)"/>
    <path class="panel-black-swoosh" d="M520 450 C590 395 630 350 655 332 L705 350 C655 430 675 520 692 610 L600 610 C570 560 545 505 520 450 Z" fill="var(--wrap-black)"/>
    <rect class="panel-red-stripe" x="292" y="590" width="372" height="12" fill="var(--wrap-red)"/>
    <rect class="panel-bumper" x="40" y="578" width="60" height="30" fill="var(--trim)"/>
    <path class="panel-front-bumper" d="M820 520 L914 520 L914 610 L820 610 Z" fill="var(--trim)"/>
  </g>

  <g class="van-glass">
    <rect class="rear-window" x="104" y="348" width="190" height="92" rx="6" fill="var(--glass)"/>
    <rect class="side-window" x="302" y="346" width="194" height="94" rx="6" fill="var(--glass)"/>
    <path class="door-window" d="M530 348 L640 348 Q670 352 690 370 L760 430 L560 452 Q530 452 530 430 Z" fill="var(--glass)"/>
    <rect class="mirror" x="662" y="405" width="26" height="30" rx="4" fill="var(--wrap-grey)"/>
  </g>

  <g class="van-wheels">
    <circle cx="228" cy="592" r="52" fill="var(--trim)"/>
    <circle cx="228" cy="592" r="40" fill="var(--wrap-black)"/>
    <circle cx="228" cy="592" r="26" fill="var(--rim)"/>
    <circle cx="748" cy="592" r="52" fill="var(--trim)"/>
    <circle cx="748" cy="592" r="40" fill="var(--wrap-black)"/>
    <circle cx="748" cy="592" r="26" fill="var(--rim)"/>
  </g>

  <g class="brand-block">
    <text class="brand-name" x="415" y="530" font-size="32" text-anchor="middle">FERNGATE</text>
    <text class="brand-name" x="415" y="574" font-size="28" text-anchor="middle">BUILDERS</text>
  </g>

  <g class="trade-badges">
    <rect class="guild-badge" x="172" y="466" width="40" height="40" fill="var(--badge)"/>
    <circle class="qtc-badge" cx="126" cy="524" r="30" fill="var(--badge)"/>
  </g>

  <text class="phone-number" x="548" y="501">02278619405</text>
</svg>
</body>
</html>
```